Book Cover - Yoga Book Front, Back, Spine

Hello - I need help with a front/back/spine design for a Sky Sling book.

Format: 6 in x 9 in
Title: SKY SLING FLOW | Manual for Living-Room Sessions
Text: https://files.quillnest.example/doc/7QXm2__r4TbnKvd8LpW3sYh9ZcNfJe5RtVu1AkGo6Pq2/view?mode=share
Other books by same author (me) https://www.pagebrook.example/shops/Dorian-Felsby/writer/K7M4P19QXT?src=wr_lnk&shop_src=wr_lnk&isPlexLinked=true&buyerHubActive=true

Target Market(s)

yoga students

Industry/Entity Type

yoga, health, fitness

Font styles to use
Sans Serif

Colors
FFF300
FFF600
FEFA6F
FFFEC7
FFFEE8
6B429C
8869AF
B7A5CE
E3DAEB
F3F0F8

Requirements
Must have
• very simple, timeless design

```html
<!DOCTYPE html>
<html lang="en">
<head>
<meta charset="utf-8">
<title>Sky Sling Flow – Cover Spread</title>
<link href="https://fonts.googleapis.com/css2?family=Montserrat:wght@400;500;600&family=Oswald:wght@500&display=swap" rel="stylesheet">
<style>
  :root {
    --purple: #8371c0;
    --yellow: #fcee21;
    --white: #ffffff;
    --ink: #111111;
    --page: #ffffff;
    --photo-dark: rgba(40, 30, 70, 0.28);
    --photo-light: rgba(183, 165, 206, 0.22);
  }
  * { margin: 0; padding: 0; box-sizing: border-box; }
  html, body { width: 900px; height: 1200px; overflow: hidden; background: var(--page); }
  .canvas { position: relative; width: 900px; height: 1200px; }

  .spread { position: absolute; left: 30px; top: 298px; width: 840px; height: 604px; }

  .back-cover { position: absolute; left: 0; top: 0; width: 403px; height: 604px; background: var(--purple); }
  .back-cover .blank-band { position: absolute; left: 0; top: 495px; width: 403px; height: 80px; background: var(--white); }
  .blurb, .author-bio {
    position: absolute; left: 42px; width: 290px;
    font-family: "Montserrat", sans-serif; font-weight: 500;
    font-size: 8.3px; line-height: 11.2px; letter-spacing: 0.45px; color: var(--white);
  }
  .blurb { top: 56px; }
  .blurb p + p { margin-top: 11px; }
  .author-bio { top: 334px; }

  .spine { position: absolute; left: 403px; top: 0; width: 34px; height: 604px; background: var(--yellow); }
  .spine-title, .spine-author {
    position: absolute; left: 50%; white-space: nowrap; color: var(--ink);
    transform-origin: 0 0; transform: rotate(90deg) translateY(-50%);
  }
  .spine-title { top: 156px; font-family: "Oswald", sans-serif; font-weight: 500; font-size: 19px; letter-spacing: 0.5px; line-height: 1; }
  .spine-author { top: 300px; font-family: "Montserrat", sans-serif; font-weight: 500; font-size: 10.5px; letter-spacing: 1.6px; line-height: 1; }

  .front-cover { position: absolute; left: 437px; top: 0; width: 403px; height: 604px; background: var(--purple); overflow: hidden; }
  .hero-circle { position: absolute; left: 98px; top: 307px; width: 194px; height: 194px; border-radius: 50%; background: var(--yellow); }
  .hero-photo {
    position: absolute; left: 52px; top: 0; width: 296px; height: 452px;
    background: linear-gradient(180deg, var(--photo-light), var(--photo-dark));
  }
  .cover-title {
    position: absolute; left: 0; top: 44px; width: 100%; text-align: center;
    font-family: "Oswald", sans-serif; font-weight: 500; font-size: 60px; line-height: 1;
    letter-spacing: 1px; color: var(--white);
  }
  .cover-subtitle {
    position: absolute; left: 0; top: 116px; width: 100%; text-align: center;
    font-family: "Montserrat", sans-serif; font-weight: 500; font-size: 13.5px; letter-spacing: 0.6px; color: var(--white);
  }
  .cover-tagline {
    position: absolute; left: 0; top: 522px; width: 100%; text-align: center;
    font-family: "Montserrat", sans-serif; font-weight: 600; font-size: 11px; letter-spacing: 0.7px; color: var(--yellow);
  }
  .cover-author {
    position: absolute; left: 0; top: 555px; width: 100%; text-align: center;
    font-family: "Montserrat", sans-serif; font-weight: 500; font-size: 21px; letter-spacing: 2.2px; color: var(--white);
  }
</style>
</head>
<body>
<div class="canvas">
  <div class="spread">
    <section class="back-cover">
      <div class="blurb">
        <p>The Sky Sling® is a fun and dynamic way to practice strength, flexibility, balance, and spinal traction at home. Regardless of age or ability, you'll learn modifications and variations that allow you to steadily develop your practice.</p>
        <p>In this guidebook, you'll learn setup and safety, setup and positions for dozens of poses. Whether you're new to inversion sling yoga or an advanced teacher, the photo-reference and step-by-step instructions make this an invaluable resource.</p>
        <p>Most people are initially drawn to the Sky Sling for at-home spinal care, but very quickly they learn how it can be used for full body, functional fitness. Let's get inverted!</p>
      </div>
      <p class="author-bio">DORIAN FELSBY is a yoga teacher, trainer, author, podcaster, and entrepreneur. He's the founder of FLOWFRAME and the FLOWFRAME Teachers College and serves as a wellness consultant for companies such as Orbitline and Nuvio. His work reaches more than two million students in eighty one countries each month. Dorian publishes weekly science-based yoga and lifestyle fitness tutorials via ClipStream, and interviews with leading health and wellness thought leaders via his podcast, The Dorian Felsby Show. You can find his published work, event, podcast and teaching schedule at www.FlowFrame.example.</p>
      <div class="blank-band"></div>
    </section>

    <section class="spine">
      <span class="spine-title">SKY SLING</span>
      <span class="spine-author">DORIAN FELSBY</span>
    </section>

    <section class="front-cover">
      <div class="hero-circle"></div>
      <div class="hero-photo" role="img" aria-label="Photo of a yoga practitioner hanging upside down in an inversion sling, legs in butterfly, arms spread wide"></div>
      <h1 class="cover-title">SKY SLING</h1>
      <p class="cover-subtitle">MANUAL FOR LIVING-ROOM SESSIONS</p>
      <p class="cover-tagline">Strength - Flexibility - Balance - Spinal Traction</p>
      <p class="cover-author">DORIAN FELSBY</p>
    </section>
  </div>
</div>
</body>
</html>
```